Webdesign für Beratung und Service im Bereich Heizungs- und Kühltechnologie
Zielgruppe
Wir sind ein modernes Dienstleistungsunternehmen, dass im Bereich Beratung und Service für Heizungs- und Kühltechnologie tätig ist. Wir suchen ein modernes Webdesign, das sich überwiegend an Geschäfts- / Gewerbekunden richten soll.
Aufgabenstellung
Wir möchten die in unserem Logo verwendete Farben auf der Webseite wiederfinden, Bilder werden mitgeliefert, müssen aber keine Verwendung finden. Wichtig ist das Hervorheben als Kundendienstvertretung des Premium-Herstellers BRK mit deren Logo und direktem Link auf deren Webseite. Gerne würden wir einen modernen Ansatz sehen, abweichend von den Standard-Seiten anderer Wartungsfirmen in unserer Branche.

```html
<!DOCTYPE html>
<html lang="de">
<head>
<meta charset="utf-8">
<title>Velotherm – Heizungs- und Kühltechnologie</title>
<link href="https://fonts.googleapis.com/css2?family=Open+Sans:ital,wght@0,400;0,600;0,700;1,700&display=swap" rel="stylesheet">
<style>
:root{
  --navy:#12305e;
  --red:#e3131b;
  --darkred:#a01e22;
  --text:#1f2a44;
  --grey:#c5ccd6;
  --line:#8fa0bf;
  --white:#fff;
}
*{box-sizing:border-box;margin:0;padding:0}
html,body{width:1200px;height:2312px;overflow:hidden;background:var(--white)}
body{position:relative;font-family:'Open Sans',sans-serif;color:var(--text)}
.abs{position:absolute}
/* header */
.brand{left:220px;top:9px;width:132px;height:38px;display:flex;align-items:center;gap:7px}
.brand-dot{width:14px;height:14px;border-radius:50%;background:var(--navy)}
.brand-name{font-size:20px;font-weight:700;color:var(--navy)}
.tagline{left:358px;top:15px;font-size:11.5px;font-weight:700;color:var(--navy);line-height:15px;text-align:center}
.topinfo{left:801px;top:8px;font-size:7px;color:var(--navy);display:flex;gap:26px}
.topinfo b{color:var(--darkred)}
.nav{left:704px;top:32px;display:flex;gap:15px;font-size:9px;color:#555}
.nav .active{color:var(--navy);font-weight:700}
/* hero */
.hero{left:0;top:56px;width:1200px;height:562px;background:radial-gradient(circle at 52% 30%,#6d6f72 0%,#3e3f41 45%,#7b7a78 100%)}
.hero-title{left:255px;top:132px;font-size:30px;font-weight:700;color:var(--white);line-height:37.5px}
.btn-emergency{left:276px;top:319px;width:163px;height:27px;background:var(--red);color:var(--white);font-weight:700;font-size:18px;display:flex;align-items:center;gap:8px;padding-left:8px;letter-spacing:.5px}
/* cards */
.band{left:0;top:904px;width:1200px;height:249px;background:var(--grey)}
.card{top:569px;width:225px;height:384px;background:var(--white);border:1px solid var(--line);text-align:center;padding:18px 12px 0}
.card h2{font-size:19.5px;font-weight:600;color:var(--navy);margin:8px 0 10px}
.card p{font-size:8.6px;line-height:13.7px;color:var(--navy)}
.card .gap{height:13.7px}
.partner{font-size:22px;font-weight:700;color:var(--red);height:36px;line-height:36px}
.product{top:969px;height:297px;width:200px;border-radius:3px}
/* emergency */
.emerg-title{left:0;width:1200px;top:1302px;text-align:center;font-size:19.5px;font-weight:600;color:var(--darkred)}
.emerg-text{left:0;width:1200px;top:1335px;text-align:center;font-size:8.7px;line-height:13.8px;color:var(--navy)}
/* contact */
.contact-title{left:0;width:1200px;top:1396px;text-align:center;font-size:19.5px;font-weight:600;color:var(--darkred)}
.contact-intro{left:236px;top:1428px;font-size:8.7px;color:var(--navy);display:flex;align-items:center;gap:4px}
.box{display:inline-block;width:10px;height:10px;border:1px solid var(--navy);border-radius:2px;margin-left:6px}
.field{top:1456px;height:18px;border:1px solid var(--line);font-size:6.5px;color:#888;padding:5px 8px}
.hint{top:1486px;font-size:6px;color:#777}
.textarea{left:244px;top:1497px;width:417px;height:40px;border:1px solid var(--navy)}
.consent{left:255px;top:1556px;font-size:6.2px;color:#777;line-height:11px;display:flex;gap:6px}
.consent .box{margin:3px 0 0}
.btn-send{left:675px;top:1556px;width:100px;height:18px;background:var(--navy);color:var(--white);font-size:10px;text-align:center;line-height:18px}
/* footer */
.footer{left:0;top:1610px;width:1200px;height:125px;background:var(--navy)}
.foot-links{left:420px;top:1639px;font-size:7.2px;font-weight:700;color:var(--white);line-height:13.1px}
.foot-brand{left:527px;top:1639px;width:140px;height:44px;background:var(--white);display:flex;align-items:center;justify-content:center;gap:7px}
.foot-tag{left:527px;top:1690px;width:140px;text-align:center;font-size:9.5px;font-weight:700;color:var(--white);line-height:15px}
.foot-addr{left:729px;top:1639px;font-size:7.2px;font-weight:700;color:var(--white);line-height:13.1px}
/* mobile */
.mobile{left:244px;top:1822px;width:201px;height:358px;overflow:hidden;background:var(--white);border:1px solid #ccc}
.m-top{height:20px;font-size:6.2px;color:var(--navy);display:flex;justify-content:flex-end;align-items:center;padding-right:8px;gap:4px}
.m-top b{color:var(--darkred)}
.m-hero{height:123px;background:radial-gradient(circle at 50% 40%,#6d6f72,#3b3c3e 60%,#7b7a78)}
.m-btn{margin:-4px auto 0;width:130px;height:20px;background:var(--red);color:var(--white);font-weight:700;font-size:14px;display:flex;align-items:center;justify-content:center;gap:6px;position:relative}
.m-title{text-align:center;font-size:13px;font-weight:600;color:var(--navy);line-height:19px;margin-top:12px}
.m-about{text-align:center;margin-top:14px}
.m-about h3{font-size:13.5px;font-weight:600;color:var(--navy);margin-top:2px}
.m-about p{font-size:8.5px;color:var(--navy);line-height:12px;margin-top:3px}
.m-menu{position:absolute;left:0;bottom:0;width:100%;height:20px;background:var(--navy);color:var(--white);font-size:9px;font-weight:700;letter-spacing:2px;display:flex;align-items:center;justify-content:space-between;padding:0 12px}
.m-menu .m-brand{font-size:9px;letter-spacing:0;background:var(--white);color:var(--navy);border-radius:8px;padding:1px 8px}
</style>
</head>
<body>

<header>
  <div class="abs brand"><span class="brand-dot"></span><span class="brand-name">Velotherm</span></div>
  <div class="abs tagline">HIGH EFFICIENT HEATING<br>AND COOLING SERVICE</div>
  <div class="abs topinfo"><span>✉ info@velotherm.de</span><span><b>Notdienst</b> +49 (0) 8000 5550123 11</span></div>
  <nav class="abs nav"><span class="active">Home</span><span>Über uns</span><span>Kundendienst BRK</span><span>Wartung</span><span>Notdienst</span><span>Kontakt</span></nav>
</header>

<section>
  <div class="abs hero" role="img" aria-label="Nahaufnahme des Lüftergitters einer Wärmepumpe"></div>
  <h1 class="abs hero-title">Ihr Spezialist für<br>Beratung und Service<br>im Bereich der<br>Heizungs- und Kühltechnologie</h1>
  <div class="abs btn-emergency">
    <svg width="20" height="20" viewBox="0 0 20 20"><circle cx="10" cy="10" r="9" fill="none" stroke="#fff" stroke-width="1.4"/><text x="10" y="13" font-size="8" fill="#fff" text-anchor="middle" font-family="Open Sans, sans-serif">24</text></svg>
    NOTDIENST
  </div>
</section>

<div class="abs band"></div>

<section>
  <article class="abs card" style="left:238px">
    <svg width="40" height="36" viewBox="0 0 40 36"><path d="M3 18 L20 3 L37 18 M8 14 V33 H32 V14 M16 33 V22 H24 V33" fill="none" stroke="#e3131b" stroke-width="2.2" stroke-linejoin="round"/></svg>
    <h2>Über uns</h2>
    <p>Wir sind ein modernes Beratungs- und Service-Unternehmen mit hochmotivierten Mitarbeitern, die seit Jahrzehnten in der Heizungs- und Klimabranche tätig sind. Unsere Mitarbeiter sind stets auf den neuesten Stand der Technik geschult. Verteilte Servicestationen machen es möglich, dass wir Ihnen deutschlandweit an 365 Tagen / 24 Stunden unsere Dienste anbieten können.</p>
    <div class="gap"></div>
    <p>Optimierte Einsatzplanung garantieren Ihnen schnelle Reaktionszeiten und schlanke Prozessstrukturen sorgen für eine reibungslose Ersatzteilversorgung. Profitieren Sie von dem tiefgreifenden Know-How unsere Mitarbeiter, ihren langjährigen Erfahrungen und dem hohen Qualitätsanspruch unseres Unternehmens.</p>
  </article>
  <article class="abs card" style="left:487px">
    <div class="partner">BRK</div>
    <h2>Kundendienst</h2>
    <p>In unserem Fokus stehen Heizungs- und Kühltechnologie mit hoher Effizienz und Rückhaltigkeit.<br>Als Kundendienstvertretung des <b><i>Schweizer Premium-Herstellers BRK</i></b>, übernehmen wir alle Kundendienstleistungen für Inbetriebnahmen, Gewährleistungs- Wartungs- und Servicearbeiten für deren Produktportfolio (u.a. Luft-Wasser oder Sole-Wasser Wärmepumpen, Splitgeräte und Serverraumkühlungen).</p>
    <div class="gap"></div>
    <p><b>Außerdem bieten wir Service und Wartungsarbeiten für folgende Produkte an:</b><br>• Klimaanlagen der Firma Norrkyl<br>• Solvane-Wärmepumpen<br>• Heizungswartungen und Austausch an Hallmer, Ostrath, Kessling etc.<br>• Solaranlagen<br>• BHKW der Firmen KWT und Enerflux</p>
  </article>
  <article class="abs card" style="left:738px">
    <svg width="40" height="36" viewBox="0 0 40 36"><path d="M6 4 L34 32 M34 4 L6 32" fill="none" stroke="#e3131b" stroke-width="3" stroke-linecap="round"/><circle cx="8" cy="6" r="4" fill="none" stroke="#e3131b" stroke-width="2"/><circle cx="32" cy="6" r="4" fill="none" stroke="#e3131b" stroke-width="2"/></svg>
    <h2>Wartung-Service</h2>
    <p>• Sorgt für einen störungsfreien Regel-Betrieb<br>• Steht für eine optimale Energiebilanz<br>• Verlängert die Lebensdauer Ihrer Anlage<br>• Erfüllt die gesetzl. Betriebsanforderungen</p>
    <div class="gap"></div>
    <p><b>Unsere Wartungs-Service umfasst:</b><br>• Kontrolle des gesamten Systems<br>• Austausch von Verschleißteilen<br>• Einstellung der Betriebsparameter<br>• Erkennen von Fehlern bevor diese ein Problem werden<br>• Sauberes, Arbeiten und transparente Information an den Kunden</p>
    <div class="gap"></div>
    <p>Wartungsverträge nach VTFA schaffen Sicherheit und Vertrauen.<br>Entscheiden Sie sich für den Spezialisten und lassen Sie sich ein individuelles Angebot für Ihre Anlagen erstellen</p>
  </article>
</section>

<section>
  <div class="abs product" style="left:248px;background:linear-gradient(160deg,#3a3a3c,#1c1c1e)" role="img" aria-label="Geöffnete Wärmepumpen-Innenanlage mit Kupferleitungen"></div>
  <div class="abs product" style="left:490px;background:linear-gradient(160deg,#e4e5e7,#b9bbbe)" role="img" aria-label="Silberne Luft-Wasser-Wärmepumpe"></div>
  <div class="abs product" style="left:735px;background:linear-gradient(160deg,#9d9a80,#6e6b57)" role="img" aria-label="Olivfarbenes Kühlaggregat mit Ventilator"></div>
</section>

<section>
  <div class="abs emerg-title">
    <svg width="34" height="34" viewBox="0 0 34 34" style="vertical-align:-10px;margin-right:6px"><path d="M6 6 Q2 16 10 26 Q18 33 26 29 L22 23 L17 25 Q11 20 10 14 L14 11 L10 4 Z" fill="none" stroke="#a01e22" stroke-width="1.4"/><circle cx="23" cy="11" r="9" fill="none" stroke="#a01e22" stroke-width="1.4"/><text x="23" y="14" font-size="9" fill="#a01e22" text-anchor="middle" font-family="Open Sans, sans-serif">24</text></svg>
    Notdienst +49 (0) 8000 5550123 11
  </div>
  <p class="abs emerg-text">Unser Notdienst steht Ihnen rund-um die Uhr für folgende Leistungen zur Verfügung:<br>Identifizieren und Beheben von Betriebs-Störungen an:<br><b>• Wärmepumpen &nbsp; • Heizungsanlagen &nbsp; • Klimaanlagen &nbsp; • Solaranlagen</b></p>
</section>

<section>
  <h2 class="abs contact-title">Kontakt zu uns</h2>
  <div class="abs contact-intro">Bitte nehmen Sie zu mit / uns unverbindlich Kontakt auf, wir möchte uns beraten lassen zu Ihren <span class="box"></span> BRK-Servicearbeiten <span class="box"></span> BRK-Wartungsarbeiten <span class="box"></span> sonstiger Hersteller</div>
  <div class="abs field" style="left:246px;width:131px">Name, Vorname*</div>
  <div class="abs field" style="left:386px;width:131px">Firma*</div>
  <div class="abs field" style="left:530px;width:131px">E-Mailadresse*</div>
  <div class="abs field" style="left:674px;width:131px">Tel. / Handy*</div>
  <div class="abs field" style="left:819px;width:131px">Gerätestandort</div>
  <div class="abs hint" style="left:255px">Bitte teilen Sie uns in Ihrer Nachricht nach Möglichkeit genauer Informationen zu Hersteller, Gerätetyp, Baujahr, Garantie und / oder Mängel mit.</div>
  <div class="abs hint" style="left:827px">*Pflichtfelder</div>
  <div class="abs textarea"></div>
  <div class="abs consent"><span class="box"></span><span>Ich habe die <u>Datenschutzerklärung</u> zur Kenntnis genommen und akzeptiert. Ich stimme zu, dass meine<br>Formularangaben zur Kontaktaufnahme bzw. zur Bearbeitung meines Anliegens gespeichert werden.</span></div>
  <div class="abs btn-send">abschicken &gt;</div>
</section>

<footer>
  <div class="abs footer"></div>
  <div class="abs foot-links">Home<br>Kontakt<br>Impressum<br>AGB<br>Datenschutz<br>Cookie-Policy</div>
  <div class="abs foot-brand"><span class="brand-dot"></span><span class="brand-name">Velotherm</span></div>
  <div class="abs foot-tag">HIGH EFFICIENT HEATING<br>AND COOLING SERVICE</div>
  <div class="abs foot-addr">Velotherm GmbH<br>Lindenweg 5b<br>85600 Musterau<br>Tel. +49 (0) 8000 5550123 11<br>Fax +49 (0) 8000 5550123 12<br>info@velotherm.de</div>
</footer>

<section class="abs mobile">
  <div class="m-top"><b>Notdienst</b> +49 (0) 8000 5550123 11</div>
  <div class="m-hero" role="img" aria-label="Lüftergitter einer Wärmepumpe"></div>
  <div class="m-btn">
    <svg width="14" height="14" viewBox="0 0 20 20"><circle cx="10" cy="10" r="9" fill="none" stroke="#fff" stroke-width="1.6"/><text x="10" y="13" font-size="8" fill="#fff" text-anchor="middle" font-family="Open Sans, sans-serif">24</text></svg>
    NOTDIENST
  </div>
  <div class="m-title">Ihr Spezialist für<br>Beratung und Service<br>im Bereich der<br>Heizungs- und Kühltechnologie</div>
  <div class="m-about">
    <svg width="30" height="28" viewBox="0 0 40 36"><path d="M3 18 L20 3 L37 18 M8 14 V33 H32 V14 M16 33 V22 H24 V33" fill="none" stroke="#e3131b" stroke-width="2.4" stroke-linejoin="round"/></svg>
    <h3>Über uns</h3>
    <p>Wir sind ein modernes Beratungs- und<br>Service-Unternehmen mit hochmotivierten</p>
  </div>
  <div class="m-menu"><span>☰ MENU</span><span class="m-brand">Velotherm</span></div>
</section>

</body>
</html>
```